Create a bold and border around my logo to make it pop and sign graphic design

I would like someone to create a sign graphic design so I can use on the side of my trucks and put on yard signs. I would to remove a lot of the white and add more of the orange and blue to give it more pop when cars drive past. I would like the services to be removed and for you to leave space for a mobile number that i would add later. I don’t want my logo changed at all. I just want colour and design to be added to the background so i can use it in signage. Same colour as on the sign

```html
<!DOCTYPE html>
<html lang="en">
<head>
<meta charset="utf-8">
<title>Timberwonders Sign</title>
<link rel="stylesheet" href="https://fonts.googleapis.com/css2?family=Lexend:wght@600&display=swap">
<style>
  :root {
    --page: #ffffff;
    --blue: #3639c6;
    --orange: #f27300;
    --white: #ffffff;
  }
  html, body {
    margin: 0;
    padding: 0;
    overflow: hidden;
    background: var(--page);
  }
  .canvas {
    position: relative;
    width: 1200px;
    height: 1000px;
    overflow: hidden;
    background: var(--page);
  }
  .sunburst {
    position: absolute;
    left: 0;
    top: 0;
  }
  .ray-blue { fill: var(--blue); }
  .ray-orange { fill: var(--orange); }
  .emblem-disc { fill: var(--white); }
  .name-plate {
    position: absolute;
    left: 258px;
    top: 617px;
    width: 688px;
    height: 81px;
    border-radius: 14px;
    background: var(--white);
    display: flex;
    align-items: center;
    justify-content: center;
  }
  .brand-name {
    margin: 0;
    font-family: "Lexend", sans-serif;
    font-weight: 600;
    font-size: 64px;
    line-height: 1;
    letter-spacing: 2px;
    color: var(--blue);
  }
</style>
</head>
<body>
<main class="canvas">
  <svg class="sunburst" width="1200" height="1000" viewBox="0 0 1200 1000">
    <g class="rays">
      <polygon class="ray-blue"   points="600,500 100,411 100,229 132,229"/>
      <polygon class="ray-orange" points="600,500 132,229 373,229"/>
      <polygon class="ray-blue"   points="600,500 373,229 501,229"/>
      <polygon class="ray-orange" points="600,500 501,229 600,229"/>
      <polygon class="ray-blue"   points="600,500 600,229 698,229"/>
      <polygon class="ray-orange" points="600,500 698,229 827,229"/>
      <polygon class="ray-blue"   points="600,500 827,229 1068,229"/>
      <polygon class="ray-orange" points="600,500 1068,229 1100,229 1100,411"/>
      <polygon class="ray-blue"   points="600,500 1100,411 1100,587"/>
      <polygon class="ray-orange" points="600,500 1100,587 1100,770 1068,770"/>
      <polygon class="ray-blue"   points="600,500 1068,770 827,770"/>
      <polygon class="ray-orange" points="600,500 827,770 698,770"/>
      <polygon class="ray-blue"   points="600,500 698,770 600,770"/>
      <polygon class="ray-orange" points="600,500 600,770 501,770"/>
      <polygon class="ray-blue"   points="600,500 501,770 373,770"/>
      <polygon class="ray-orange" points="600,500 373,770 132,770"/>
      <polygon class="ray-blue"   points="600,500 132,770 100,770 100,587"/>
      <polygon class="ray-orange" points="600,500 100,587 100,411"/>
    </g>
    <circle class="emblem-disc" cx="600" cy="450" r="145" role="img" aria-label="Company emblem area"/>
  </svg>
  <div class="name-plate">
    <h1 class="brand-name">TIMBERWONDERS</h1>
  </div>
</main>
</body>
</html>
```